Lena Corvell Business Card

I need a business card that reflects my current website: itslenacorvell.example and screenshot attached. If we keep the color scheme of the site and sample card below that would be ideal. The business card should include the information on the attached sample cards.

Industry/Entity Type

Business

```html
<!DOCTYPE html>
<html lang="en">
<head>
<meta charset="utf-8">
<title>Lena Corvell Business Card</title>
<link rel="stylesheet" href="https://fonts.googleapis.com/css2?family=Lato:ital,wght@0,400;0,700;1,400&display=swap">
<style>
  :root {
    --backdrop: #2b2b2b;
    --card-white: #f7f7f7;
    --band-black: #050505;
    --teal: #3cbfa3;
    --ink: #111111;
    --text-light: #d9d9d9;
    --text-muted: #bdbdbd;
    --photo-warm: #c9a98a;
    --photo-denim: #6f8fb0;
  }
  * { box-sizing: border-box; margin: 0; padding: 0; }
  html, body {
    width: 1200px; height: 900px; overflow: hidden;
    background: var(--backdrop);
  }
  .card {
    position: absolute; left: 110px; top: 170px;
    width: 980px; height: 560px;
    background: var(--card-white);
    border-top: 6px solid var(--teal);
    overflow: hidden;
    font-family: "Lato", Arial, sans-serif;
  }
  .card__band {
    position: absolute; left: 0; right: 0; top: 336px; bottom: 0;
    background: var(--band-black);
    border-top: 8px solid var(--teal);
    border-bottom: 16px solid var(--teal);
  }
  .card__photo {
    position: absolute; right: 40px; top: 22px;
    width: 280px; height: 280px;
    border: 4px solid var(--teal); border-radius: 30px;
    padding: 8px; background: var(--card-white);
  }
  .card__photo-fill {
    width: 100%; height: 100%; border-radius: 22px;
    background: linear-gradient(180deg, #efe6da 0%, var(--photo-warm) 45%, var(--photo-denim) 100%);
  }
  .card__name {
    position: absolute; left: 90px; top: 150px;
    color: var(--ink); font-weight: 700; font-size: 64px; line-height: 1;
    white-space: nowrap;
  }
  .card__tagline {
    position: absolute; left: 80px; top: 372px;
    color: var(--text-light); font-style: italic; font-size: 20px;
  }
  .card__site {
    position: absolute; left: 80px; top: 404px;
    color: #ffffff; font-weight: 700; font-size: 21px;
    display: flex; align-items: center; gap: 10px;
  }
  .card__phone {
    position: absolute; left: 80px; top: 452px;
    color: var(--text-muted); font-size: 22px; letter-spacing: 1px;
    display: flex; flex-direction: column; align-items: center; gap: 4px;
  }
  .card__handle {
    position: absolute; left: 420px; top: 436px;
    color: var(--text-muted); font-size: 22px;
  }
  .card__email {
    position: absolute; right: 50px; top: 372px;
    color: var(--text-muted); font-size: 22px;
    display: flex; flex-direction: column; align-items: center; gap: 6px;
  }
  .icon { fill: none; stroke: currentColor; stroke-width: 2; }
</style>
</head>
<body>
  <div class="card">
    <div class="card__photo">
      <div class="card__photo-fill" role="img" aria-label="Portrait photograph of Lena Corvell"></div>
    </div>
    <div class="card__name">Lena Corvell</div>

    <div class="card__band"></div>

    <p class="card__tagline">Brand Curator | Digital Storyteller | Social Entrpreneur</p>
    <p class="card__site">
      <svg class="icon" width="18" height="18" viewBox="0 0 18 18" aria-hidden="true">
        <path d="M7 11 L11 7"/>
        <path d="M8 5 L10 3 a3 3 0 0 1 5 5 L13 10"/>
        <path d="M10 13 L8 15 a3 3 0 0 1 -5 -5 L5 8"/>
      </svg>
      www.itslenacorvell.example
    </p>
    <div class="card__phone">
      <svg width="26" height="20" viewBox="0 0 26 20" aria-hidden="true" fill="currentColor">
        <path d="M2 7 Q13 -1 24 7 L21 9 L18 6 L8 6 L5 9 Z"/>
        <rect x="6" y="9" width="14" height="9" rx="2"/>
      </svg>
      <span>555.014.2290</span>
    </div>
    <p class="card__handle">@itslenacorvell</p>
    <div class="card__email">
      <svg class="icon" width="24" height="16" viewBox="0 0 24 16" aria-hidden="true">
        <rect x="1" y="1" width="22" height="14"/>
        <path d="M1 1 L12 9 L23 1"/>
      </svg>
      <span>me@lenacorvell.example</span>
    </div>
  </div>
</body>
</html>
```